Brookfarrow Osteopathy and dry needling business card

Business card for Brookfarrow Osteopathy and Dry Needling.

Industry/Entity Type

Health

Contact Information for Business Card

I do not have a phone number yet. I also do not have an email address yet. The physical address is: 48 Lower Crane Street Brookfarrow The website is: www.brookfarrowosteosteopathy.example My details are: Dr Martin Pellowe, Osteopath (B.Clin.Sci (Ost) M.Ost BSC ECON (Hons)

Colors
0094D4
00A9DD
6FCCEA
C7EBF8
E9F6FB

Requirements
Must have
• logo on the back
Nice to have
• Maybe a space for me to write an appointment time and date on the card.

```html
<!DOCTYPE html>
<html lang="en">
<head>
<meta charset="utf-8">
<title>Brookfarrow Osteopathy and Dry Needling – Business Card</title>
<link href="https://fonts.googleapis.com/css2?family=Lato:wght@300;400&display=swap" rel="stylesheet">
<style>
  :root{
    --blue:#0094d4;
    --blue-bright:#00a9dd;
    --blue-deep:#0a86c6;
    --orange:#f7931e;
    --paper:#ffffff;
    --stage:#e9f6fb;
  }
  *{margin:0;padding:0;box-sizing:border-box}
  html,body{width:1200px;height:900px;overflow:hidden}
  body{
    background:var(--stage);
    font-family:"Lato",Arial,sans-serif;
    display:flex;flex-direction:column;align-items:center;justify-content:center;gap:60px;
  }
  .card{
    width:630px;height:360px;position:relative;
    box-shadow:0 10px 30px rgba(0,60,100,.18);
  }
  /* Front */
  .card--front{background:var(--paper);display:flex;align-items:center}
  .brand{
    width:270px;display:flex;flex-direction:column;align-items:center;gap:16px;
    color:var(--blue);text-align:center;
  }
  .brand__ring{width:70px;height:70px;border:2px solid var(--blue);border-radius:50%}
  .brand__name{font-weight:400;font-size:19px;letter-spacing:2px;text-transform:uppercase;line-height:1.4;text-align:center}
  .divider{width:2px;height:230px;background:var(--blue)}
  .details{flex:1;padding:0 36px 0 32px;color:var(--blue)}
  .person{text-align:right;margin-bottom:26px}
  .person__name{
    font-weight:300;font-size:30px;color:var(--blue-bright);
    border-bottom:2px solid var(--orange);padding-bottom:4px;display:inline-block;
  }
  .person__role{font-weight:300;font-size:21px;margin-top:6px;color:var(--blue-bright)}
  .person__credentials{font-weight:300;font-size:12.5px;margin-top:4px;color:var(--blue-bright);white-space:nowrap}
  .contact{list-style:none;display:flex;flex-direction:column;gap:12px}
  .contact__item{display:flex;align-items:center;gap:14px;font-weight:300;font-size:15.5px;white-space:nowrap}
  .contact__icon{width:16px;height:16px;flex:none}
  /* Back */
  .card--back{
    background:linear-gradient(160deg,var(--blue-bright) 0%,var(--blue) 60%,var(--blue-deep) 100%);
    display:flex;flex-direction:column;align-items:center;justify-content:center;gap:18px;color:#fff;
  }
  .card--back .brand__ring{border-color:#fff;width:90px;height:90px}
  .card--back .brand__name{color:#fff;font-size:20px}
</style>
</head>
<body>
  <section class="card card--front" aria-label="Business card front">
    <div class="brand">
      <div class="brand__ring"></div>
      <p class="brand__name">Brookfarrow<br>Osteopathy &amp;<br>Dry Needling</p>
    </div>
    <div class="divider"></div>
    <div class="details">
      <div class="person">
        <p class="person__name">Dr Martin Pellowe</p>
        <p class="person__role">Osteopath</p>
        <p class="person__credentials">B.Clin.Sci (Ost) M.Ost BSC ECON (Hons)</p>
      </div>
      <ul class="contact">
        <li class="contact__item">
          <svg class="contact__icon" viewBox="0 0 16 16"><g fill="none" stroke="var(--orange)" stroke-width="1.6" stroke-linecap="round"><path d="M2 2.5a11.5 11.5 0 0 1 11.5 11.5"/><path d="M2 6.5a7.5 7.5 0 0 1 7.5 7.5"/></g><circle cx="3" cy="13" r="1.7" fill="var(--orange)"/></svg>
          <span>brookfarrowosteosteopathy.example</span>
        </li>
        <li class="contact__item">
          <svg class="contact__icon" viewBox="0 0 16 16"><path d="M8 15s5-5.2 5-8.8A5 5 0 0 0 3 6.2C3 9.8 8 15 8 15z" fill="var(--orange)"/><circle cx="8" cy="6.3" r="2" fill="#fff"/></svg>
          <span>48 Lower Crane Street Brookfarrow</span>
        </li>
      </ul>
    </div>
  </section>

  <section class="card card--back" aria-label="Business card back">
    <div class="brand__ring"></div>
    <p class="brand__name">Brookfarrow Osteopathy<br>&amp; Dry Needling</p>
  </section>
</body>
</html>
```